Meridale Freightworks Group - needs a website

Build a simple but professional website for Meridale Freightworks Group.
Web address is www.merfregro.com.au
We have just completed developing a brochure and the contents of the brochure would serve as the web pages.
Web design does not need to deviate far from the brochure and will not include electronic commerce etc at this stage.

Target Market(s)

Privately owned logistics businesses in Australia

Industry/Entity Type

Build

Number of Pages Required

5+ page

Requirements
Must have
• Professional, elegant, ability to upload video in the future, ability to add e-commerce in the future

```html
<!DOCTYPE html>
<html lang="en">
<head>
<meta charset="utf-8">
<title>Meridale Freightworks Group</title>
<link href="https://fonts.googleapis.com/css2?family=Roboto:wght@300;400;500&display=swap" rel="stylesheet">
<style>
:root{
  --navy:#123f8c;
  --navy-deep:#0b3a84;
  --ink:#5c6673;
  --slate:#707e8b;
  --slate-line:#c9d0d6;
  --white:#ffffff;
  --muted:#8792a0;
  --dark:#1d1f22;
}
*{box-sizing:border-box;margin:0;padding:0}
html,body{width:1200px;height:2951px;overflow:hidden}
body{font-family:"Roboto",Arial,sans-serif;font-weight:300;color:var(--ink);background:var(--white)}
.canvas{position:relative;width:1200px;height:2951px;overflow:hidden}
.abs{position:absolute}

/* header */
.top{left:0;top:0;width:1200px;height:614px;background:linear-gradient(180deg,#f4f5f6 0%,#e6e9ec 100%)}
.brand{left:100px;top:34px;display:flex;align-items:center;gap:12px;font-size:24px;font-weight:500;color:var(--navy)}
.brand-mark{width:34px;height:34px;background:var(--navy)}
.phone-pill{left:962px;top:40px;height:26px;width:140px;border-radius:13px;background:#3d4a5c;color:#fff;font-size:15px;display:flex;align-items:center;gap:8px;padding-left:4px}
.phone-pill .dot{width:20px;height:20px;border-radius:50%;background:var(--navy);display:flex;align-items:center;justify-content:center}
.nav{left:424px;top:78px;display:flex;font-size:15px;font-weight:400;color:#4a5564}
.nav a{color:inherit;text-decoration:none;margin-right:46px}
.nav a.active{color:var(--navy)}
.nav a:last-child{margin-right:0}

.hero-photo{left:100px;top:118px;width:700px;height:448px;background:linear-gradient(135deg,#5a5e63 0%,#a9a59b 45%,#c7c0ae 70%,#6b6a66 100%)}
.hero-panel{left:800px;top:118px;width:301px;height:448px;background:var(--navy-deep);text-align:center;color:#fff}
.hero-panel h1{font-weight:300;font-size:37px;line-height:44px;margin-top:100px}
.btn-grey{display:inline-block;margin-top:48px;width:158px;height:46px;line-height:46px;background:#c9cdd2;color:#fff;font-size:14px;font-weight:400}

/* welcome */
.welcome{left:0;top:614px;width:1200px;height:385px;background:var(--slate);color:#fff}
.welcome h2{position:absolute;left:130px;top:62px;width:280px;text-align:center;font-weight:300;font-size:30px;line-height:44px}
.welcome .rule{position:absolute;left:418px;top:40px;width:1px;height:305px;background:var(--slate-line)}
.welcome p{position:absolute;left:458px;top:68px;width:605px;font-size:15px;line-height:25px;font-weight:400}
.btn-white{position:absolute;left:458px;top:275px;width:160px;height:48px;line-height:48px;background:#fff;color:#4a5564;text-align:center;font-size:14px;font-weight:400}

/* pillars */
.pillars{left:0;top:999px;width:1200px;height:586px;background:#fff}
.pillars h2{position:absolute;top:50px;width:100%;text-align:center;font-weight:300;font-size:34px;color:var(--navy)}
.pillar{position:absolute;top:188px;width:330px;text-align:center}
.pillar .map{width:172px;height:146px;margin:0 auto;background:linear-gradient(180deg,#f1f3f5,#e2e6ea);border-radius:18px}
.pillar h3{font-weight:300;font-size:30px;color:var(--navy);margin-top:18px}
.pillar p{font-size:15px;line-height:25px;color:var(--muted);margin:14px auto 0;width:300px}

/* video */
.video{left:0;top:1585px;width:1200px;height:523px;background:var(--slate);color:#fff}
.video h2{position:absolute;top:36px;width:100%;text-align:center;font-weight:300;font-size:33px}
.player{position:absolute;left:183px;top:107px;width:820px;height:366px;box-shadow:0 16px 22px rgba(0,0,0,.35)}
.player .frame{width:820px;height:328px;background:linear-gradient(90deg,#b24a2a 0%,#5d7a63 30%,#d9d6cc 50%,#5d7a63 70%,#b24a2a 100%)}
.player .bar{width:820px;height:38px;background:var(--dark);position:relative;font-size:14px;font-weight:400}
.player .progress{position:absolute;left:0;top:0;width:820px;height:5px;background:#555}
.player .progress span{display:block;width:190px;height:5px;background:#c1121f}
.player .play{position:absolute;left:368px;top:122px}
.player .time{position:absolute;left:128px;top:14px}
.player .quality{position:absolute;right:90px;top:14px}

/* team */
.team{left:0;top:2108px;width:1200px;height:600px;background:radial-gradient(ellipse at 60% 30%,#4f7fc4 0%,#1f56a8 45%,#0e3d8c 100%);color:#fff}
.team h2{position:absolute;top:64px;width:100%;text-align:center;font-weight:300;font-size:33px}
.member{position:absolute;top:154px;width:330px;text-align:center}
.member .portrait{width:200px;height:200px;margin:0 auto;border-radius:50%;background:linear-gradient(180deg,#c9ccd1,#6f7882)}
.member h3{font-weight:300;font-size:20px;margin-top:32px}
.member p{font-size:15px;line-height:26px;font-weight:400;margin:14px auto 0;width:280px}
.member .more{width:14px;height:14px;margin:20px auto 0;background:#fff;color:var(--navy);font-size:13px;line-height:14px;font-weight:500}

/* footer */
.footer{left:0;top:2708px;width:1200px;height:184px;background:#fff;font-size:12px;font-weight:400;color:#6b7684}
.footer .foot-brand{position:absolute;left:112px;top:40px;font-size:15px;font-weight:500;color:var(--navy);width:150px;line-height:20px}
.footer ul{position:absolute;top:40px;list-style:none}
.footer li{height:21px;line-height:21px;padding-left:20px;position:relative}
.footer li::before{content:"";position:absolute;left:2px;top:7px;border-left:5px solid #6b7684;border-top:3.5px solid transparent;border-bottom:3.5px solid transparent}
.contact{position:absolute;left:612px;top:40px;line-height:21px}
.contact .row{display:flex;gap:10px}
.contact .ico{width:14px;color:var(--navy)}
.legal{left:0;top:2892px;width:1200px;height:59px;border-top:1px solid #e8eaed;background:#fff;text-align:center;font-size:12px;font-weight:400;color:#6b7684;line-height:42px}
</style>
</head>
<body>
<div class="canvas">

  <div class="abs top"></div>
  <div class="abs brand"><span class="brand-mark"></span>Meridale Freightworks Group</div>
  <div class="abs phone-pill"><span class="dot">
    <svg width="12" height="12" viewBox="0 0 24 24"><path fill="#fff" d="M6.6 10.8a15 15 0 0 0 6.6 6.6l2.2-2.2a1 1 0 0 1 1-.25 11.4 11.4 0 0 0 3.6.57 1 1 0 0 1 1 1V20a1 1 0 0 1-1 1A17 17 0 0 1 3 4a1 1 0 0 1 1-1h3.5a1 1 0 0 1 1 1c0 1.25.2 2.450.57 3.57a1 1 0 0 1-.25 1z"/></svg>
  </span>07 3100 5820</div>
  <nav class="abs nav">
    <a class="active" href="#">HOME</a><a href="#">ABOUT US</a><a href="#">SERVICES</a><a href="#">SOLUTIONS</a><a href="#">OUR TEAM</a><a href="#">CONTACT US</a>
  </nav>

  <div class="abs hero-photo" role="img" aria-label="Warehouse interior with forklifts and tall pallet racking"></div>
  <div class="abs hero-panel">
    <h1>WE ARE<br>MERIDALE<br>FREIGHTWORKS<br>GROUP</h1>
    <span class="btn-grey">LEARN MORE</span>
  </div>

  <section class="abs welcome">
    <h2>WELCOME<br>TO MERIDALE<br>FREIGHTWORKS<br>GROUP</h2>
    <div class="rule"></div>
    <p>Sed ut perspiciatis unde omnis iste natus error sit voluptatem accusantium doloremque laudantium, totam rem aperiam, eaque ipsa quae ab illo inventore veritatis et quasi architecto beatae vitae dicta sunt explicabo. Nemo enim ipsam voluptatem quia voluptas sit aspernatur aut odit aut fugit, sed quia consequuntur magni dolores eos qui ratione voluptatem sequi nesciunt. Neque porro quisquam est, qui dolorem ipsum quia dolor sit amet, consectetur, adipisci velit, sed quia non numquam eius modi tempora incidunt ut labore et dolore magnam aliquam quaerat voluptatem.</p>
    <span class="btn-white">LEARN MORE</span>
  </section>

  <section class="abs pillars">
    <h2>MERIDALE FREIGHTWORKS GROUP</h2>
    <div class="pillar" style="left:100px">
      <div class="map" role="img" aria-label="Outline map of Australia with a scale icon"></div>
      <h3>Scale</h3>
      <p>Sed ut perspiciatis unde omnis iste natus error sit voluptatem accusantium doloremque laudantium, totam rem aperiam, eaque ipsa quae ab illo inventore veritatis et quasi architecto beatae vitae</p>
    </div>
    <div class="pillar" style="left:435px">
      <div class="map" role="img" aria-label="Outline map of Australia with a triangle pattern icon"></div>
      <h3>Synergy</h3>
      <p>Sed ut perspiciatis unde omnis iste natus error sit voluptatem accusantium doloremque laudantium, totam rem aperiam, eaque ipsa quae ab illo inventore veritatis et quasi architecto beatae vitae</p>
    </div>
    <div class="pillar" style="left:770px">
      <div class="map" role="img" aria-label="Outline map of Australia with a house and dollar icon"></div>
      <h3>Value</h3>
      <p>Sed ut perspiciatis unde omnis iste natus error sit voluptatem accusantium doloremque laudantium, totam rem aperiam, eaque ipsa quae ab illo inventore veritatis et quasi architecto beatae vitae</p>
    </div>
  </section>

  <section class="abs video">
    <h2>FEATURED VIDEO</h2>
    <div class="player">
      <div class="frame" role="img" aria-label="Video still of a long warehouse aisle with orange racking"></div>
      <svg class="play" width="84" height="84" viewBox="0 0 84 84"><circle cx="42" cy="42" r="38" fill="none" stroke="#fff" stroke-width="7"/><path d="M33 26 L60 42 L33 58 Z" fill="#fff"/></svg>
      <div class="bar">
        <div class="progress"><span></span></div>
        <svg style="position:absolute;left:30px;top:14px" width="14" height="16" viewBox="0 0 14 16"><rect x="1" y="0" width="4" height="16" fill="#fff"/><rect x="9" y="0" width="4" height="16" fill="#fff"/></svg>
        <svg style="position:absolute;left:84px;top:13px" width="22" height="18" viewBox="0 0 22 18"><path d="M0 6h5l6-5v16l-6-5H0z" fill="#fff"/><path d="M14 5q3 4 0 8M17 2q6 7 0 14" stroke="#fff" stroke-width="2" fill="none"/></svg>
        <span class="time">0:02 / 0:10</span>
        <span class="quality">720p</span>
      </div>
    </div>
  </section>

  <section class="abs team">
    <h2>OUR TEAM</h2>
    <div class="member" style="left:101px">
      <div class="portrait" role="img" aria-label="Portrait photo of team member Owen Tarrant"></div>
      <h3>Owen Tarrant</h3>
      <p>Sed ut perspiciatis unde omnis iste natus error sit voluptatem accusantium doloremque laudantium</p>
      <div class="more">+</div>
    </div>
    <div class="member" style="left:435px">
      <div class="portrait" role="img" aria-label="Portrait photo of team member Leon Ashby"></div>
      <h3>Leon Ashby</h3>
      <p>Sed ut perspiciatis unde omnis iste natus error sit voluptatem accusantium doloremque laudantium</p>
      <div class="more">+</div>
    </div>
    <div class="member" style="left:769px">
      <div class="portrait" role="img" aria-label="Portrait photo of team member Dean Harlow"></div>
      <h3>Dean Harlow</h3>
      <p>Sed ut perspiciatis unde omnis iste natus error sit voluptatem accusantium doloremque laudantium</p>
      <div class="more">+</div>
    </div>
  </section>

  <footer class="abs footer">
    <div class="foot-brand">Meridale Freightworks Group</div>
    <ul style="left:294px">
      <li>Home</li><li>About Us</li><li>Services</li><li>Solutions</li><li>Our Team</li><li>Contact Us</li>
    </ul>
    <ul style="left:446px">
      <li>Terms Of Use</li><li>Privacy Policy</li><li>Legal Notice</li>
    </ul>
    <div class="contact">
      <div class="row"><span class="ico">&#9990;</span><span>:&nbsp; 07 3100 5820</span></div>
      <div class="row"><span class="ico"></span><span>&nbsp;&nbsp;&nbsp; 0400 618 275</span></div>
      <div class="row" style="margin-top:21px"><span class="ico">&#9993;</span><span>:&nbsp; d.harlow@merfregro.com.au</span></div>
      <div class="row"><span class="ico">&#9635;</span><span>:&nbsp; merfregro.com.au</span></div>
    </div>
    <ul style="left:862px">
      <li>Social Page</li><li style="margin-top:10px">News Feed</li>
    </ul>
  </footer>
  <div class="abs legal">© 2015 Meridale Freightworks Group | All Rights Reserved</div>

</div>
</body>
</html>
```